Morning Harvest Psalm Journal for the Weary Traveler on the Narrow Road

This is not an Eastern meditation method. No images or themes from guru style or Eastern meditations from Hinduism or Buddhism will work. This is a Biblical Christian-based method. Some sort of Divine Light from Heaven may be the look. Some "ancient scroll" for the title to be written in may work.

```html
<!DOCTYPE html>
<html lang="en">
<head>
<meta charset="utf-8">
<title>Morning Harvest Psalm Journal – Book Cover Wrap</title>
<link rel="stylesheet" href="https://fonts.googleapis.com/css2?family=Cinzel:wght@400;500;600&family=UnifrakturMaguntia&display=swap">
<style>
  :root {
    --page-bg: #cbbfbd;
    --sky-rose: #c9566a;
    --sky-peach: #f0b48a;
    --sky-cream: #f6efe2;
    --sky-gold: #f7c53a;
    --sun-white: #fffbe6;
    --sun-yellow: #ffd21e;
    --rock-amber: #8a5a1f;
    --rock-brown: #4e3114;
    --rock-dark: #2b1b0c;
    --spine-black: #050505;
    --parchment-light: #ecd19a;
    --parchment-mid: #d8b06a;
    --parchment-dark: #b07e3c;
    --ink-black: #0e0a06;
    --ink-white: #ffffff;
    --ink-back: #1a0f06;
  }
  * { box-sizing: border-box; margin: 0; padding: 0; }
  html, body {
    width: 1200px; height: 800px; overflow: hidden;
    background: var(--page-bg);
  }
  .stage { position: relative; width: 1200px; height: 800px; }

  .cover-wrap {
    position: absolute; left: 110px; top: 36px;
    width: 980px; height: 728px;
    display: flex;
  }

  /* Back cover */
  .back-cover { position: relative; width: 467px; height: 100%; overflow: hidden; }
  .back-photo {
    position: absolute; inset: 0;
    background:
      linear-gradient(180deg,
        var(--sky-rose) 0%, #e08a6e 14%, var(--sky-peach) 26%,
        var(--sky-cream) 38%, #f6d88c 48%, var(--sky-gold) 54%,
        #e0902c 58%, var(--rock-amber) 61%, var(--rock-brown) 75%,
        #6b4a22 88%, var(--rock-dark) 100%);
  }
  .back-blurb {
    position: absolute; left: 76px; top: 76px; width: 360px;
    font-family: "Cinzel", serif; font-size: 10.6px; line-height: 15.8px;
    color: var(--ink-back); text-align: center; font-weight: 500;
  }

  /* Spine */
  .spine {
    position: relative; width: 47px; height: 100%;
    background: var(--spine-black);
  }
  .spine-title {
    position: absolute; left: 50%; top: 228px;
    transform: translateX(-50%) rotate(90deg) translateX(50%);
    transform-origin: center;
    white-space: nowrap;
    font-family: "UnifrakturMaguntia", serif; font-size: 25px;
    color: var(--ink-white);
  }
  .spine-title, .spine-author { writing-mode: vertical-rl; transform: translateX(-50%); }
  .spine-author {
    position: absolute; left: 50%; top: 525px;
    font-family: "Cinzel", serif; font-size: 10px; letter-spacing: 4px;
    color: var(--ink-white);
  }

  /* Front cover */
  .front-cover { position: relative; width: 466px; height: 100%; overflow: hidden; }
  .front-photo {
    position: absolute; inset: 0;
    background:
      radial-gradient(ellipse 120px 80px at 46% 63%, var(--sun-white) 0%, rgba(255,232,120,.9) 40%, rgba(255,210,30,0) 100%),
      radial-gradient(ellipse 140px 260px at 46% 82%, rgba(214,180,120,.75) 0%, rgba(214,180,120,0) 100%),
      linear-gradient(180deg,
        #d9b39a 0%, var(--sky-cream) 14%, #efd9b8 26%,
        #e9a778 34%, #f6d98a 44%, var(--sun-yellow) 54%,
        #f4a81c 59%, #a8701f 64%, var(--rock-brown) 76%,
        #7a5a2c 88%, #5c4220 100%);
  }
  .title-scroll {
    position: absolute; left: 30px; top: 90px; width: 396px; height: 164px;
    border-radius: 6px;
    background: linear-gradient(90deg,
      var(--parchment-dark) 0%, var(--parchment-mid) 6%, var(--parchment-light) 30%,
      var(--parchment-light) 70%, var(--parchment-mid) 94%, var(--parchment-dark) 100%);
    box-shadow: 0 4px 10px rgba(60,30,0,.35);
  }
  .front-title {
    position: absolute; left: 30px; top: 104px; width: 396px;
    text-align: center;
    font-family: "UnifrakturMaguntia", serif; font-weight: 400;
    font-size: 50px; line-height: 64px; color: var(--ink-black);
  }
  .front-subtitle {
    position: absolute; left: 0; top: 316px; width: 100%;
    text-align: center;
    font-family: "Cinzel", serif; font-weight: 500;
    font-size: 24px; line-height: 31px; color: var(--ink-black);
  }
  .front-author {
    position: absolute; left: 0; top: 592px; width: 100%;
    text-align: center;
    font-family: "Cinzel", serif; font-weight: 500;
    font-size: 22px; letter-spacing: 6px; color: var(--ink-white);
  }
</style>
</head>
<body>
<main class="stage">
  <section class="cover-wrap">
    <div class="back-cover">
      <div class="back-photo" role="img" aria-label="Photograph of a rose and gold sunset sky over a dark rocky cliff landscape"></div>
      <p class="back-blurb">Sed ut perspiciatis unde omnis iste natus error sit voluptatem accusantium doloremque laudantium, totam rem aperiam, eaque ipsa quae ab illo inventore veritatis et quasi architecto beatae vitae dicta sunt explicabo. Nemo enim ipsam voluptatem quia voluptas sit aspernatur aut odit aut fugit, sed quia consequuntur magni dolores eos qui ratione voluptatem sequi nesciunt. Neque porro quisquam est, qui dolorem ipsum quia dolor sit amet, consectetur, adipisci velit, sed quia non numquam eius modi tempora incidunt ut labore et dolore magnam aliquam quaerat voluptatem. Ut enim ad minima veniam, quis nostrum exercitationem ullam corporis suscipit laboriosam, nisi ut aliquid ex ea commodi consequatur? Quis autem vel eum iure reprehenderit qui in ea voluptate velit esse quam nihil molestiae consequatur, vel illum qui dolorem eum fugiat quo voluptas nulla pariatur?”</p>
    </div>

    <div class="spine">
      <span class="spine-title">Morning Harvest</span>
      <span class="spine-author">THOMAS ELLERY</span>
    </div>

    <div class="front-cover">
      <div class="front-photo" role="img" aria-label="Photograph of radiant golden sunlight bursting over a waterfall between rocky cliffs beneath a glowing sky"></div>
      <div class="title-scroll" role="img" aria-label="Illustration of an unrolled ancient parchment scroll"></div>
      <h1 class="front-title">Morning Harvest<br>Psalm Journal</h1>
      <p class="front-subtitle">FOR THE WEARY TRAVELER<br>ON THE NARROW ROAD</p>
      <p class="front-author">THOMAS ELLERY</p>
    </div>
  </section>
</main>
</body>
</html>
```